International Freight forwarder needs a flyer design

We are an International Freight forwarder and we would like to let everyone know that we ship boats around the globe.
We would like our logo on the flyer, plus the 3 photos i have attached and our contact details including web page
www.cargowinq.com and contact details that are below for Dana Morrow.

wording could be?

Cargowinq Ships Boats!

We ship Race boats, Sail boats, new boats, used boats, pontoon boats, ski boats, fishing boats, house boats, cruising boats, well you get the picture "YOUR BOAT"

Contact Dana Morrow for a quote:
dana.morrow@cargowinq.com
+1 555 384 7629

Target Market(s)

boat manufacturers, boat retailers, boat import and export companies, boat wholesalers

Font styles to use
Sans Serif

Requirements
Must have
• Logo and contact details

```html
<!DOCTYPE html>
<html lang="en">
<head>
<meta charset="utf-8">
<title>Cargowinq Ships Boats – Flyer</title>
<link rel="stylesheet" href="https://fonts.googleapis.com/css2?family=Roboto+Condensed:ital,wght@0,400;0,700;1,700&family=Roboto:wght@400&display=swap">
<style>
  :root{
    --stage:#e9ecef;
    --paper:#ffffff;
    --ink:#111111;
    --red:#e31e24;
    --navy:#2a2f6e;
    --sea:#3c4f9a;
    --grey:#8a8a8a;
    --swoosh:#b9b9bd;
    --night:#0d0b0c;
  }
  *{margin:0;padding:0;box-sizing:border-box}
  html,body{width:1200px;height:1200px;overflow:hidden;background:var(--stage)}
  .flyer{position:absolute;left:330px;top:28px;width:540px;height:1144px;background:var(--paper);overflow:hidden;
    font-family:"Roboto Condensed",Arial,sans-serif;color:var(--ink);box-shadow:0 10px 30px rgba(0,0,0,.25)}
  .flyer-shapes{position:absolute;inset:0}
  .brand{position:absolute;left:74px;top:73px;display:flex;align-items:center;gap:40px}
  .brand-dot{width:70px;height:70px;border-radius:50%;background:var(--red)}
  .brand-name{font-weight:700;font-size:46px;line-height:1;letter-spacing:.5px;color:var(--ink)}
  .tagline{position:absolute;left:0;right:0;top:344px;text-align:center;color:#fff;font-weight:700;font-size:22.5px;line-height:24px}
  .headline{position:absolute;left:54px;top:420px;font-weight:700;font-size:36px;line-height:1;white-space:nowrap}
  .headline .accent{color:var(--red)}
  .boat-list{position:absolute;top:460px;list-style:none;font-size:22px;line-height:36.5px}
  .boat-list li{position:relative;padding-left:22px}
  .boat-list li::before{content:"";position:absolute;left:0;top:12px;width:12px;height:12px;border-radius:50%;background:var(--red)}
  .boat-list.col-a{left:76px}
  .boat-list.col-b{left:289px}
  .picture-line{position:absolute;left:54px;top:638px;white-space:nowrap;line-height:36px}
  .picture-line .lead{font-size:22px;color:var(--grey)}
  .picture-line .your-boat{font-weight:700;font-size:36px;color:var(--red);margin-left:4px}
  .offices{position:absolute;left:0;right:0;top:874px;text-align:center;color:#fff;font-family:"Roboto",Arial,sans-serif;font-size:17.5px;line-height:21px}
  .countries{position:absolute;left:0;right:0;top:926px;text-align:center;font-size:18.8px;line-height:22px;color:var(--ink)}
  .contact{position:absolute;left:0;right:0;top:1032px;text-align:center;color:#fff;font-size:28px;line-height:32px}
  .contact .person{color:var(--red);font-weight:700;font-style:italic}
  .contact-details{position:absolute;left:0;right:0;top:1067px;text-align:center;color:#fff;font-family:"Roboto",Arial,sans-serif;font-size:17.5px;line-height:22px}
  .contact-details .sep{margin:0 12px}
</style>
</head>
<body>
<div class="flyer">
  <svg class="flyer-shapes" width="540" height="1144" viewBox="0 0 540 1144">
    <defs>
      <linearGradient id="seaFade" x1="0" y1="0" x2="0" y2="1">
        <stop offset="0" stop-color="#ffffff"/>
        <stop offset=".32" stop-color="#c9cde6"/>
        <stop offset=".6" stop-color="var(--sea)"/>
        <stop offset="1" stop-color="var(--navy)"/>
      </linearGradient>
      <radialGradient id="photoTone" cx=".45" cy=".4" r=".7">
        <stop offset="0" stop-color="#c8cdd3"/>
        <stop offset="1" stop-color="#4b5a70"/>
      </radialGradient>
    </defs>
    <g role="img" aria-label="Photo of a motor yacht speeding across deep blue sea with white wake">
      <path d="M0 0H540V378Q300 382 0 398Z" fill="url(#seaFade)"/>
    </g>
    <path d="M0 398Q300 382 540 378V392Q300 398 0 414Z" fill="var(--swoosh)"/>
    <path d="M315 688Q400 677 490 683" stroke="var(--red)" stroke-width="3.5" fill="none" stroke-linecap="round"/>
    <path d="M0 813Q120 820 250 838Q420 828 540 780V984Q300 990 0 1017Z" fill="var(--red)"/>
    <path d="M0 1017Q300 990 540 984V1144H0Z" fill="var(--swoosh)"/>
    <path d="M0 1033Q300 1000 540 996V1144H0Z" fill="var(--night)"/>
    <g role="img" aria-label="Photo of a boat being lifted by crane at a dock">
      <circle cx="114" cy="764" r="70" fill="url(#photoTone)" stroke="var(--red)" stroke-width="6"/>
    </g>
    <g role="img" aria-label="Photo of a shrink-wrapped boat on a cradle inside a warehouse">
      <circle cx="270" cy="780" r="70" fill="url(#photoTone)" stroke="var(--red)" stroke-width="6"/>
    </g>
    <g role="img" aria-label="Photo of a shrink-wrapped boat on a trailer inside a warehouse">
      <circle cx="426" cy="764" r="70" fill="url(#photoTone)" stroke="var(--red)" stroke-width="6"/>
    </g>
  </svg>

  <div class="brand"><span class="brand-dot"></span><span class="brand-name">CARGOWINQ</span></div>
  <p class="tagline">INTERNATIONAL FREIGHT FOR HEAVY MACHINERY</p>

  <h1 class="headline"><span class="accent">CARGOWINQ</span> SHIPS BOATS!</h1>
  <ul class="boat-list col-a">
    <li>RACE BOATS</li><li>SAIL BOATS</li><li>NEW BOATS</li><li>USED BOATS</li><li>PONTOON BOATS</li>
  </ul>
  <ul class="boat-list col-b">
    <li>SKI BOATS</li><li>FISHING BOATS</li><li>HOUSE BOATS</li><li>CRUISING BOATS</li>
  </ul>
  <p class="picture-line"><span class="lead">WELL YOU GET THE PICTURE</span><span class="your-boat">"YOUR BOAT"</span></p>

  <p class="offices">With offices worldwide Cargowinq is available to you anytime!<br>Contact a Cargowinq representative now.</p>
  <p class="countries">AUSTRALIA | CANADA | USA | GERMANY | THAILAND | JAPAN</p>

  <p class="contact">CONTACT <span class="person">DANA MORROW</span> FOR A QUOTE:</p>
  <p class="contact-details">dana.morrow@cargowinq.com<span class="sep">|</span>+1 555 384 7629</p>
</div>
</body>
</html>
```